Wine label

I'm wanting to create a wine label that is very very simple, but eye catching. Jump off the shelf.

Name of Winery : Morrow Ridge

Nothing on the front but that - will be putting other info on back - which will be the brand label.

I was thinking of something MR - possibly - with morrow ridge intertwined. -

1 color label and possible 1 or 2 ink

```html
<!DOCTYPE html>
<html lang="en">
<head>
<meta charset="utf-8">
<title>Morrow Ridge – Wine Label</title>
<link rel="stylesheet" href="https://fonts.googleapis.com/css2?family=Questrial&family=Italianno&display=swap">
<style>
  :root {
    --backdrop: #e9e7e3;
    --label-paper: #f6f6f4;
    --label-edge: #dcdcd8;
    --ink-charcoal: #3a3a3a;
    --ink-silver: #9ea3a8;
    --ink-pattern: #b9bcbf;
  }
  html, body {
    margin: 0;
    padding: 0;
    width: 1200px;
    height: 844px;
    overflow: hidden;
    background: var(--backdrop);
  }
  .canvas {
    position: relative;
    width: 1200px;
    height: 844px;
  }
  .wine-label {
    position: absolute;
    left: 312px;
    top: 77px;
    width: 576px;
    height: 690px;
    background: var(--label-paper);
    border: 1px solid var(--label-edge);
    box-sizing: border-box;
  }
  .winery-name {
    position: absolute;
    top: 164px;
    left: 0;
    right: 0;
    margin: 0;
    text-align: center;
    font-family: "Questrial", sans-serif;
    font-weight: 400;
    font-size: 56px;
    line-height: 64px;
    letter-spacing: 4px;
    color: var(--ink-charcoal);
  }
  .brand-mark {
    position: absolute;
    top: 262px;
    left: 0;
    right: 0;
    display: flex;
    justify-content: center;
    align-items: center;
    gap: 22px;
  }
  .brand-mark__dot {
    width: 14px;
    height: 14px;
    border-radius: 50%;
    background: var(--ink-silver);
  }
  .brand-mark__name {
    font-family: "Questrial", sans-serif;
    font-size: 120px;
    line-height: 1;
    letter-spacing: 6px;
    color: var(--ink-silver);
  }
  .vineyard-line {
    position: absolute;
    top: 505px;
    left: 0;
    right: 0;
    margin: 0;
    text-align: center;
    font-family: "Italianno", cursive;
    font-size: 54px;
    line-height: 60px;
    color: var(--ink-charcoal);
  }
  .border-ornament {
    position: absolute;
    top: 598px;
    left: 72px;
    width: 348px;
    height: 52px;
    background: linear-gradient(to bottom, var(--ink-pattern), #c9cbcd);
  }
</style>
</head>
<body>
  <main class="canvas">
    <section class="wine-label">
      <h1 class="winery-name">MORROW RIDGE</h1>
      <div class="brand-mark">
        <span class="brand-mark__name">MR</span>
        <span class="brand-mark__dot"></span>
      </div>
      <p class="vineyard-line">Vineyard Morrow Ridge</p>
      <div class="border-ornament" role="img" aria-label="Silver Greek key border ornament"></div>
    </section>
  </main>
</body>
</html>
```